Business Card Design

Lotside Ledger is an online automotive resource on a national scale specifically targeting lease purchases for new cars. Our Online and app platform allow prospective lease clients to scan a window sticker while at a franchise dealership and instantly receive a lease quote at what we call the sweet spot. Lotside Ledger offers price transparency during the lease process to allow average people the confidence in the lease process and takes away any fear of the big franchise dealers.
Lotside ledger allows ordinary lease customers to know they are getting a low price lease and not overpaying. Never overpay again

Industry/Entity Type

Automotive

Contact Information for Business Card

Lotside Ledger
Marcus Todwell (President of operations)
Phone: 888-302-7716
Cell: 561-448-2053

```html
<!DOCTYPE html>
<html lang="en">
<head>
<meta charset="utf-8">
<title>Lotside Ledger – Business Card</title>
<link rel="stylesheet" href="https://fonts.googleapis.com/css2?family=Arimo:wght@400;700&display=swap">
<style>
  :root {
    --backdrop: #4a413b;
    --card: #1c1c1c;
    --card-edge: #262626;
    --ink: #ffffff;
    --ink-soft: #e6e6e6;
    --emboss: #2f2f2f;
  }
  * { margin: 0; padding: 0; box-sizing: border-box; }
  html, body {
    width: 1200px;
    height: 827px;
    overflow: hidden;
    background: var(--backdrop);
    font-family: "Arimo", Arial, sans-serif;
  }
  .sheet {
    position: relative;
    width: 1200px;
    height: 827px;
    display: flex;
    align-items: center;
    justify-content: center;
    gap: 40px;
  }
  .card {
    position: relative;
    width: 540px;
    height: 309px;
    background: var(--card);
    border: 1px solid var(--card-edge);
  }
  .brand {
    position: absolute;
    display: flex;
    align-items: center;
    gap: 16px;
    font-weight: 700;
    text-transform: uppercase;
    line-height: 0.92;
  }
  .brand-dot {
    width: 40px;
    height: 40px;
    border-radius: 50%;
    flex: none;
  }
  .brand-name { font-size: 52px; letter-spacing: -1px; }

  .card--back .brand { left: 120px; top: 98px; }
  .card--back .brand-dot { background: var(--emboss); }
  .card--back .brand-name { color: var(--emboss); }

  .card--front .brand { left: 150px; top: 46px; }
  .card--front .brand-dot { background: var(--ink); }
  .card--front .brand-name { color: var(--ink); }

  .holder {
    position: absolute;
    left: 0;
    right: 0;
    top: 180px;
    text-align: center;
    color: var(--ink-soft);
    font-size: 17px;
    line-height: 1.2;
  }
  .holder-name { text-transform: uppercase; letter-spacing: 0.5px; }
  .contacts {
    position: absolute;
    left: 60px;
    right: 60px;
    top: 238px;
    display: flex;
    justify-content: space-between;
    color: var(--ink-soft);
    font-size: 18px;
  }
  .contact { display: flex; align-items: center; gap: 6px; }
  .contact svg { width: 16px; height: 18px; fill: none; stroke: var(--ink); stroke-width: 1.6; }
</style>
</head>
<body>
<main class="sheet">
  <section class="card card--back" aria-label="Card back">
    <div class="brand">
      <span class="brand-dot"></span>
      <span class="brand-name">Lotside<br>Ledger</span>
    </div>
  </section>

  <section class="card card--front" aria-label="Card front">
    <div class="brand">
      <span class="brand-dot"></span>
      <span class="brand-name">Lotside<br>Ledger</span>
    </div>
    <div class="holder">
      <p class="holder-name">Marcus Todwell</p>
      <p class="holder-title">President of operations</p>
    </div>
    <div class="contacts">
      <p class="contact">
        <svg viewBox="0 0 16 18" aria-hidden="true"><path d="M4 2 L7 5 L5.5 7.5 Q7 11 10.5 12.5 L13 11 L15 14 L12.5 16 Q4 14 2 4.5 Z"/></svg>
        888-302-7716
      </p>
      <p class="contact">
        <svg viewBox="0 0 16 18" aria-hidden="true"><rect x="3.5" y="1" width="9" height="16" rx="1.5"/><line x1="6.5" y1="14.5" x2="9.5" y2="14.5"/></svg>
        561-448-2053
      </p>
    </div>
  </section>
</main>
</body>
</html>
```